We need a cover designed for our book on parenting. The focus of this book is on the parents, not on the child! We like the idea of this title having a double meaning - insight as in gaining insights into parenting, and "in sight" as in looking inward as parents and how to improve ourselves rather than looking outward to improve our children. We would love for the cover to somehow represent this double meaning. I can upload an excerpt from the book soon over the next few days.
Updates

Reason: We are still reviewing the amazing designs! Thank you so much! :)

Target Market(s)

Parents with kids of any age from babies through adult children.

Requirements
Must have
• Title is: Steady Hearth Homes
• Subtitle is: Building Calm Households Daily
• Authors names: Tara Bellwin, LCSW Dorian Bellwin, Ph.D.

```html
<!DOCTYPE html>
<html lang="en">
<head>
<meta charset="utf-8">
<title>Steady Hearth Homes — Book Cover</title>
<link rel="stylesheet" href="https://fonts.googleapis.com/css2?family=Anton&family=Dancing+Script:wght@700&family=Oswald:wght@300;500;600;700&family=Playfair+Display&display=swap">
<style>
  :root {
    --cream: #fdf9d0;
    --sun: #f7b716;
    --sun-deep: #f29a12;
    --sun-light: #fbc82a;
    --ink: #0b0a0a;
    --brown: #3a1d0c;
    --script: #f5bd1c;
  }
  * { margin: 0; padding: 0; box-sizing: border-box; }
  html, body { width: 1200px; height: 914px; overflow: hidden; background: var(--cream); }
  .cover { position: relative; width: 1200px; height: 914px; overflow: hidden; }

  .panel { position: absolute; }
  .back-quote { left: 0; top: 0; width: 588px; height: 430px; background: var(--cream); }
  .back-about {
    left: 0; top: 430px; width: 588px; height: 484px;
    background: radial-gradient(circle at 70% 95%, var(--sun-deep) 0%, transparent 55%),
                linear-gradient(160deg, var(--sun-light), var(--sun) 55%, var(--sun-deep));
  }
  .front-top {
    left: 588px; top: 0; width: 612px; height: 428px;
    background: radial-gradient(circle at 72% 12%, var(--sun-deep) 0%, transparent 45%),
                linear-gradient(180deg, var(--sun) 0%, var(--sun-light) 70%, var(--sun) 100%);
    border-bottom: 1px solid var(--ink);
  }
  .front-bottom { left: 588px; top: 429px; width: 612px; height: 485px; background: var(--cream); }

  .quote-heading {
    position: absolute; left: 30px; top: 34px;
    font: 26px "Playfair Display", serif; color: var(--ink);
  }
  .quote-body {
    position: absolute; left: 30px; top: 121px; width: 519px;
    font: 300 21px/26.4px "Oswald", sans-serif; color: var(--brown);
    text-align: justify; text-indent: 8px;
  }
  .quote-body strong { font-weight: 600; }

  .author-photo { position: absolute; left: 26px; top: 458px; width: 205px; height: 259px; background: var(--cream); }
  .author-bio {
    position: absolute; left: 242px; top: 460px; width: 322px;
    font: 300 22px/30.4px "Oswald", sans-serif; color: var(--brown);
    text-align: justify;
  }

  .family-silhouettes {
    position: absolute; left: 632px; top: 146px; width: 548px; height: 152px;
    background: linear-gradient(180deg, rgba(11,10,10,0.35), rgba(11,10,10,0.75));
    border-radius: 60px 60px 6px 6px;
  }
  .title-art { position: absolute; left: 588px; top: 0; width: 612px; height: 600px; overflow: visible; }
  .title-main { font-family: "Anton", sans-serif; font-size: 178px; fill: var(--ink); }
  .title-script { font-family: "Dancing Script", cursive; font-weight: 700; font-size: 104px; fill: var(--script); }

  .subtitle { position: absolute; left: 600px; width: 600px; text-align: center; font-family: "Oswald", sans-serif; }
  .subtitle-1 { top: 558px; font-weight: 500; font-size: 44px; color: var(--ink); }
  .subtitle-2 { top: 616px; font-weight: 500; font-size: 38px; color: var(--script); }
  .subtitle-3 { top: 668px; font-weight: 700; font-size: 60px; color: var(--ink); }
  .authors {
    position: absolute; left: 600px; top: 858px; width: 600px; text-align: center;
    font: 31px "Playfair Display", serif; color: var(--ink);
  }
</style>
</head>
<body>
<div class="cover">
  <section class="panel back-quote"></section>
  <section class="panel back-about"></section>
  <section class="panel front-top"></section>
  <section class="panel front-bottom"></section>

  <h2 class="quote-heading">"A quote from the book"</h2>
  <p class="quote-body"><strong>Lorem ipsum dolor sit amet, consetetur sadipscing elitr, sed diam nonumy eirmod tempor</strong> invidunt ut labore et dolore magna aliquyam erat, sed diam voluptua. At vero eos et accusam et justo duo dolores et ea rebum. Stet clita kasd gubergren, no sea takimata sanctus est Lorem ipsum dolor sit amet. Lorem ipsum dolor sit amet, consetetur sadipscing elitr, sed diam nonumy eirmod tempor invidunt ut labore et dolore magna aliquyam erat, sed diam voluptua. At vero eos et accusam et justo duo dolores et ea rebum. Stet clita kasd gubergren, no sea takimata sanctus est Lorem ipsum dolor sit amet.</p>

  <div class="author-photo"></div>
  <p class="author-bio">Lorem ipsum dolor sit amet, consetetur sadipscing elitr, sed diam nonumy eirmod tempor invidunt ut labore et dolore magna aliquyam erat, sed diam voluptua. At vero eos et accusam et justo duo dolores et ea rebum.</p>

  <div class="family-silhouettes" role="img" aria-label="Black silhouettes of parents and children playing together, standing on top of the title letters"></div>

  <svg class="title-art" viewBox="0 0 612 600" aria-label="Steady Hearth Homes">
    <text class="title-main" x="60" y="428" textLength="532" lengthAdjust="spacingAndGlyphs">STEADY</text>
    <text class="title-script" x="64" y="522" textLength="512" lengthAdjust="spacingAndGlyphs">Hearth Homes</text>
  </svg>

  <p class="subtitle subtitle-1">Building Calm</p>
  <p class="subtitle subtitle-2">Households</p>
  <p class="subtitle subtitle-3">Daily</p>
  <p class="authors">Tara Bellwin, LCSW Dorian Bellwin, Ph.D.</p>
</div>
</body>
</html>
```